WordPress Website for Pain Relief Clinic

I need a WordPress website designed for my laser pain relief clinic. It needs to be a professional, responsive design with 7 pages: Home, Why Choose Us, Treatable Conditions, Testimonials, FAQ, Franchising, Contact Us. Here is logo: https://files.brivoltcdn.com/media.t-w-e-n.com/sitebuilder/472/CalvexaLogoHighQuality.png

Target Market(s)

people with pain,elderly adults,injuries,soreness

Industry/Entity Type

Clinic

Number of Pages Required

5+ page

Colors
0792cd
85abd2

```html
<!DOCTYPE html>
<html lang="en">
<head>
<meta charset="utf-8">
<title>Calvexa – Laser Pain Relief Clinic</title>
<link href="https://fonts.googleapis.com/css2?family=Open+Sans:wght@400;600;700&display=swap" rel="stylesheet">
<style>
:root{
  --brand:#0792cd;
  --brand-soft:#85abd2;
  --ink:#333a40;
  --muted:#6b7278;
  --line:#d6dde3;
  --dark:#3b3f44;
  --darker:#2f3236;
  --white:#ffffff;
}
*{box-sizing:border-box;margin:0;padding:0}
html,body{width:1200px;height:2452px;overflow:hidden;background:var(--white)}
body{font-family:"Open Sans",Arial,sans-serif;color:var(--ink);position:relative}
.site-header{position:absolute;left:0;top:0;width:1200px;height:144px}
.brand{position:absolute;left:76px;top:26px;display:flex;align-items:center;gap:12px}
.brand-mark{width:22px;height:22px;background:var(--brand)}
.brand-name{font-size:42px;font-weight:700;color:var(--brand);letter-spacing:-1px}
.main-nav{position:absolute;left:152px;top:112px;width:1008px;height:32px;background:var(--brand);display:flex;justify-content:space-around;align-items:center}
.main-nav a{color:var(--white);font-size:13px;text-decoration:none}
.hero{position:absolute;left:0;top:144px;width:1200px;height:440px;
  background:
    radial-gradient(ellipse 260px 220px at 330px 180px,rgba(255,255,255,.95),rgba(255,255,255,0) 70%),
    radial-gradient(ellipse 200px 160px at 980px 150px,rgba(133,171,210,.75),rgba(133,171,210,0) 70%),
    radial-gradient(ellipse 220px 120px at 520px 360px,rgba(214,170,150,.7),rgba(214,170,150,0) 70%),
    linear-gradient(90deg,#6f7c87 0%,#c9d2d9 30%,#eef1f3 55%,#d5dde3 75%,#8e9ba6 100%)}
.hero-arrow{position:absolute;top:190px;width:40px;height:60px}
.hero-dots{position:absolute;left:0;right:0;bottom:40px;display:flex;justify-content:center;gap:24px}
.hero-dots span{width:12px;height:12px;border-radius:50%;background:var(--white);opacity:.85}
.hero-rule{position:absolute;left:0;top:584px;width:1200px;height:8px;background:var(--brand)}
.section-title{position:absolute;left:0;width:1200px;text-align:center;font-size:30px;font-weight:600;color:var(--brand)}
.lead{position:absolute;left:140px;width:920px;text-align:center;font-size:14px;line-height:24px;color:var(--ink)}
.btn-outline{position:absolute;height:34px;padding:0 20px;border:1px solid var(--line);color:var(--brand);font-size:14px;line-height:32px;background:var(--white)}
.service{position:absolute;top:880px;width:480px}
.service-photo{width:480px;height:268px}
.service-photo.back{background:
    radial-gradient(ellipse 160px 110px at 210px 130px,rgba(7,146,205,.55),rgba(7,146,205,0) 70%),
    linear-gradient(135deg,#b9826a 0%,#dcb3a0 40%,#efe0d6 65%,#8b969f 100%)}
.service-photo.shoulder{background:
    radial-gradient(ellipse 140px 120px at 300px 120px,rgba(133,171,210,.6),rgba(133,171,210,0) 70%),
    linear-gradient(135deg,#8a96a0 0%,#dfe5e9 45%,#f2ece7 65%,#c49a86 100%)}
.service h3{margin-top:16px;font-size:20px;font-weight:700;color:var(--brand)}
.service p{margin-top:6px;font-size:14px;line-height:25px;color:var(--ink)}
.service .btn-outline{position:static;display:inline-block;margin-top:20px}
.reviews{position:absolute;left:0;top:1472px;width:1200px;height:360px;background:linear-gradient(90deg,#2c2f33,#4b5056 50%,#2c2f33)}
.reviews .section-title{top:28px}
.quote-mark{position:absolute;left:180px;top:100px}
.review-text{position:absolute;left:288px;top:110px;width:280px;font-size:14px;line-height:22px;color:#d8dde1}
.review-author{position:absolute;left:288px;top:240px;width:280px;text-align:right;font-size:13px;line-height:20px;color:#d8dde1}
.review-photo{position:absolute;left:592px;top:90px;width:456px;height:256px;background:
    radial-gradient(ellipse 120px 130px at 250px 150px,rgba(90,110,125,.7),rgba(90,110,125,0) 70%),
    linear-gradient(135deg,#7fa6c6 0%,#cddbe6 50%,#e9ecee 70%,#76848f 100%)}
.review-bars{position:absolute;left:300px;bottom:0;display:flex;gap:26px}
.review-bars span{width:100px;height:4px;background:#9aa2a8}
.review-bars span.active{background:var(--white)}
.appointment-title{position:absolute;left:620px;top:1928px;font-size:20px;font-weight:400;color:var(--brand)}
.field{position:absolute;left:728px;width:264px;height:40px;border:1px solid var(--line);font-size:13px;color:#9aa1a7;text-align:center;line-height:38px}
.field.message{height:112px;line-height:30px}
.btn-solid{position:absolute;left:806px;top:2232px;width:104px;height:38px;background:var(--brand);color:var(--white);font-size:14px;line-height:38px;text-align:center}
.contact{position:absolute;left:152px;top:2024px}
.contact h4{font-size:22px;font-weight:600;color:var(--darker)}
.contact p{font-size:13px;line-height:20px;color:var(--ink)}
.contact .company{margin-top:14px;font-weight:700}
.site-footer{position:absolute;left:0;top:2332px;width:1200px;height:120px;background:var(--dark)}
.footer-nav{position:absolute;left:132px;top:30px;width:936px;display:flex;justify-content:space-between}
.footer-nav a{color:#d3d7db;font-size:13px;text-decoration:none}
.footer-rule{position:absolute;left:132px;top:66px;width:936px;height:1px;background:#5a5f65}
.copyright{position:absolute;left:0;top:84px;width:1200px;text-align:center;font-size:11px;color:#9ba1a7}
</style>
</head>
<body>
<header class="site-header">
  <div class="brand"><span class="brand-mark"></span><span class="brand-name">Calvexa</span></div>
  <nav class="main-nav">
    <a href="#">Home</a><a href="#">Why Choose Us</a><a href="#">Treatable Conditions</a><a href="#">Testimonials</a><a href="#">FAQ</a><a href="#">Franchising</a><a href="#">Contact Us</a>
  </nav>
</header>

<section class="hero" role="img" aria-label="Clinician applying a handheld laser therapy device to a patient's knee in a treatment room">
  <svg class="hero-arrow" style="left:50px" viewBox="0 0 40 60"><polyline points="30,6 8,30 30,54" fill="none" stroke="#fff" stroke-width="6"/></svg>
  <svg class="hero-arrow" style="right:50px" viewBox="0 0 40 60"><polyline points="10,6 32,30 10,54" fill="none" stroke="#fff" stroke-width="6"/></svg>
  <div class="hero-dots"><span></span><span></span><span></span><span></span><span></span></div>
</section>
<div class="hero-rule"></div>

<h2 class="section-title" style="top:586px;padding-top:20px">Welcome</h2>
<p class="lead" style="top:648px">At Calvexa we help people live with less pain. Our clinic uses gentle, drug-free laser therapy to ease sore joints, sports injuries, back and neck pain, and the everyday aches that come with age. Each visit is quick and comfortable, and every plan is shaped around you by a caring team who listen first and treat second, so you can move freely again.</p>
<span class="btn-outline" style="left:546px;top:762px">Read more</span>

<h2 class="section-title" style="top:836px">Our Services</h2>
<article class="service" style="left:120px">
  <div class="service-photo back" role="img" aria-label="Laser therapy device applied to a patient's lower back"></div>
  <h3>Laser Therapy</h3>
  <p>Our low-level laser therapy sends soft light deep into tissue to calm swelling, speed healing and relieve pain without pills or surgery. Sessions last only a few minutes and need no downtime, so you can return to work, family and the things you love the same day. Most patients feel real change after a short course of care.</p>
  <span class="btn-outline">Read more</span>
</article>
<article class="service" style="left:608px">
  <div class="service-photo shoulder" role="img" aria-label="Therapist treating a patient's shoulder with a laser device"></div>
  <h3>Joint Care</h3>
  <p>Stiff shoulders, knees and hips can make simple tasks hard. Our joint care program blends targeted laser sessions with easy movement advice to restore comfort and range of motion. It is well suited to older adults, people recovering from injury and anyone living with arthritis or long-term soreness who wants a gentle path back to activity.</p>
  <span class="btn-outline">Read more</span>
</article>

<section class="reviews">
  <h2 class="section-title" style="font-size:24px">Our Patients Review</h2>
  <svg class="quote-mark" width="96" height="80" viewBox="0 0 96 80" fill="var(--brand)">
    <path d="M6 44 Q6 12 40 4 L42 14 Q22 20 22 38 L40 38 L40 76 L6 76 Z"/>
    <path d="M54 44 Q54 12 88 4 L90 14 Q70 20 70 38 L88 38 L88 76 L54 76 Z"/>
  </svg>
  <p class="review-text">Before coming here, I could barely walk because of my knee. After the treatment everything is better. I can go back to work. Excellent treatment!!</p>
  <p class="review-author">Daniel Morrow<br>CA</p>
  <div class="review-photo" role="img" aria-label="Patient seated in the clinic in front of anatomy charts"></div>
  <div class="review-bars"><span class="active"></span><span></span><span></span><span></span><span></span><span></span></div>
</section>

<h3 class="appointment-title">Get Appointment Right now!!!</h3>
<div class="field" style="top:1988px">Name</div>
<div class="field" style="top:2048px">Email</div>
<div class="field message" style="top:2108px">Message</div>
<div class="btn-solid">Book Now</div>

<div class="contact">
  <h4>CONTACT US</h4>
  <p class="company">CALVEXA</p>
  <p>1-555-010-7720 Oak Street, Suite 4</p>
  <p>hello@calvexa-clinic.com</p>
</div>

<footer class="site-footer">
  <nav class="footer-nav">
    <a href="#">Home</a><a href="#">Why Choose Us</a><a href="#">Treatable Conditions</a><a href="#">Testimonials</a><a href="#">FAQ</a><a href="#">Franchising</a><a href="#">Contact Us</a>
  </nav>
  <div class="footer-rule"></div>
  <p class="copyright">Copyright © 2024 Calvexa Laser Pain Relief Clinic. All rights reserved. Designed with care.</p>
</footer>
</body>
</html>
```